7Brink Plumbing flyer

I want to incorporate our logo design into a new flyer promoting the business and advertising products that we install.
We install hot water systems, Air-conditioning systems and central heating systems. Along with other aspects of plumbing such as gasfitting, roofing, sanitary and drainage
I would like the background to be the same as our business cards with the water effect and colours.

Requirements
Must have
• Logo
24/7 Emergency call out
Aspects of plumbing we do
- Hot water systems
- Central Heating
- Solar hot water systems/ heat pump systems
- Gasfitting
- Drainage
- Roofing
- Air-Conditioning
Nice to have
• Pictures of hot water systems and air-conditioning system
$30 off voucher when producing this flyer (limit 1 per house hold)

```html
<!DOCTYPE html>
<html lang="en">
<head>
<meta charset="utf-8">
<title>7Brink Plumbing Flyer</title>
<link href="https://fonts.googleapis.com/css2?family=Exo+2:wght@500;600;700&display=swap" rel="stylesheet">
<style>
  :root {
    --page-bg: #d9d9d9;
    --paper: #ffffff;
    --brand-blue: #1f6fb8;
    --sky-blue: #2aa8ec;
    --light-blue: #5cc4f7;
    --deep-blue: #0d4f9a;
    --ink: #1a1a1a;
    --white: #ffffff;
  }
  * { margin: 0; padding: 0; box-sizing: border-box; }
  html, body { width: 1200px; height: 1000px; overflow: hidden; }
  body { background: var(--page-bg); font-family: "Exo 2", sans-serif; position: relative; }

  .flyer {
    position: absolute; left: 290px; top: 66px;
    width: 613px; height: 866px;
    background: var(--paper); overflow: hidden;
  }
  .waves { position: absolute; inset: 0; }

  .brand {
    position: absolute; left: 44px; top: 42px; z-index: 3;
    display: flex; align-items: center; gap: 40px;
  }
  .brand-dot { width: 74px; height: 74px; border-radius: 50%; background: var(--brand-blue); }
  .brand-name {
    color: var(--brand-blue); font-weight: 700; font-size: 36px; line-height: 38px;
    text-transform: uppercase; letter-spacing: 0.5px;
  }

  .hero-photo {
    position: absolute; left: 355px; top: 18px; width: 250px; height: 462px; z-index: 2;
    border-radius: 110px 110px 40px 150px;
    background: linear-gradient(180deg, #e9e4df 0%, #d3cdc7 32%, #2f4d8a 52%, #22386a 100%);
  }

  .headline { position: absolute; left: 45px; top: 332px; text-transform: uppercase; z-index: 2; }
  .headline span { display: block; }
  .headline-brand { color: var(--light-blue); font-weight: 700; font-size: 48px; line-height: 54px; }
  .headline-line { color: var(--white); font-weight: 600; font-size: 26px; line-height: 32px; letter-spacing: 0.5px; }
  .headline-line.accent { color: var(--light-blue); }

  .services {
    position: absolute; left: 42px; top: 546px; width: 529px; z-index: 2;
    display: grid; grid-template-columns: 251px 251px; column-gap: 27px; row-gap: 8px;
    list-style: none;
  }
  .service {
    height: 34px; border-radius: 12px;
    background: linear-gradient(180deg, #47c0fa 0%, #1596e0 100%);
    box-shadow: 0 3px 0 #0c5fa3;
    color: var(--white); font-weight: 600; font-size: 15px;
    display: flex; align-items: center; justify-content: center;
    text-transform: uppercase; letter-spacing: 0.3px;
  }

  .contact { position: absolute; left: 40px; top: 749px; z-index: 2; }
  .contact-name { color: var(--sky-blue); font-weight: 700; font-size: 21px; line-height: 24px; text-transform: uppercase; margin-bottom: 8px; }
  .contact-row { display: flex; align-items: center; gap: 12px; color: var(--ink); font-weight: 600; height: 24px; }
  .contact-row svg { width: 13px; height: 13px; flex: none; }
  .contact-row.phone { font-size: 22px; }
  .contact-row.mail, .contact-row.web { font-size: 18px; }

  .photo-circle { position: absolute; border-radius: 50%; border: 4px solid var(--sky-blue); z-index: 2; }
  .photo-house { left: 325px; top: 722px; width: 134px; height: 134px; background: linear-gradient(135deg, #c9c4bb, #8a5a3c 60%, #3f7a3a); }
  .photo-van { left: 455px; top: 718px; width: 180px; height: 180px; background: linear-gradient(180deg, #cfd9df 0%, #b7bcbf 50%, #5d8c45 100%); }
</style>
</head>
<body>
  <main class="flyer">
    <svg class="waves" viewBox="0 0 613 866" width="613" height="866">
      <defs>
        <linearGradient id="band-blue" x1="0" y1="0" x2="0" y2="1">
          <stop offset="0" stop-color="#1b74c4"/>
          <stop offset="1" stop-color="#2aa8ec"/>
        </linearGradient>
        <linearGradient id="band-pale" x1="0" y1="0" x2="1" y2="0">
          <stop offset="0" stop-color="#c7d3e6"/>
          <stop offset="1" stop-color="#7a93c2"/>
        </linearGradient>
        <radialGradient id="dark-field" cx="0.4" cy="0.45" r="0.75">
          <stop offset="0" stop-color="#55585d"/>
          <stop offset="0.6" stop-color="#2e3034"/>
          <stop offset="1" stop-color="#16181b"/>
        </radialGradient>
      </defs>
      <g aria-hidden="true">
        <path d="M0 160 C120 140 240 175 340 230 C430 280 520 270 613 240 L613 420 L0 420 Z" fill="url(#band-blue)"/>
        <path d="M0 230 C140 215 260 250 360 295 C450 330 530 320 613 300 L613 420 L0 420 Z" fill="url(#band-pale)"/>
      </g>
      <g role="img" aria-label="Dark background covered with water droplets">
        <path d="M0 275 C150 258 270 290 370 330 C460 360 540 350 613 335 L613 866 L0 866 Z" fill="url(#dark-field)"/>
      </g>
      <g aria-hidden="true">
        <circle cx="445" cy="374" r="165" fill="none" stroke="#3a7cc0" stroke-width="22" opacity="0.85"/>
        <path d="M0 724 C140 718 250 730 340 752 C440 776 530 760 613 740 L613 866 L0 866 Z" fill="#2a6fb8"/>
        <path d="M0 734 C140 728 250 740 340 762 C440 786 530 770 613 752 L613 866 L0 866 Z" fill="var(--paper)"/>
      </g>
    </svg>

    <div class="brand">
      <span class="brand-dot"></span>
      <span class="brand-name">7Brink<br>Plumbing</span>
    </div>

    <div class="hero-photo" role="img" aria-label="Smiling plumber in blue overalls holding a pipe wrench and tool bag"></div>

    <h1 class="headline">
      <span class="headline-brand">7Brink</span>
      <span class="headline-line">Plumbing is a</span>
      <span class="headline-line">local plumbing</span>
      <span class="headline-line">business</span>
      <span class="headline-line accent">Specializing in</span>
    </h1>

    <ul class="services">
      <li class="service">Plumbing and Gasfitting</li>
      <li class="service">Central Heating</li>
      <li class="service">Air-Conditioning</li>
      <li class="service">Roofing</li>
      <li class="service">Blocked Drains</li>
      <li class="service">Sanitary and Drainage</li>
      <li class="service">Hot Water Systems</li>
      <li class="service">Solar Hot Water</li>
    </ul>

    <section class="contact">
      <p class="contact-name">Liam Brink</p>
      <p class="contact-row phone">
        <svg viewBox="0 0 16 16"><path d="M3 1 L6 1 L7 5 L5 6 C6 8 8 10 10 11 L11 9 L15 10 L15 13 C15 14 14 15 13 15 C6 15 1 10 1 3 C1 2 2 1 3 1 Z" fill="#2aa8ec"/></svg>
        0400 555 123
      </p>
      <p class="contact-row mail">
        <svg viewBox="0 0 16 16"><rect x="1" y="3" width="14" height="10" fill="#2aa8ec"/><path d="M1 3 L8 9 L15 3" fill="none" stroke="#fff" stroke-width="1.5"/></svg>
        Liam@7brinkplumbing.com
      </p>
      <p class="contact-row web">
        <svg viewBox="0 0 16 16"><circle cx="8" cy="8" r="7" fill="none" stroke="#2aa8ec" stroke-width="1.5"/><path d="M1 8 H15 M8 1 C5 5 5 11 8 15 M8 1 C11 5 11 11 8 15" fill="none" stroke="#2aa8ec" stroke-width="1.2"/></svg>
        www.7brinkplumbing.com
      </p>
    </section>

    <div class="photo-circle photo-van" role="img" aria-label="Work ute with toolboxes parked on a street"></div>
    <div class="photo-circle photo-house" role="img" aria-label="Hot water unit installed on a brick house wall"></div>
  </main>
</body>
</html>
```